Brava-Lux.ch is looking for business card letterhead and envelope C5 with WOW effect

We need a strong business card for our company Brava-Lux.ch, logo is available. You want a black or dark background on which the logo Stark r% 26 # 252; appears. Letterhead and envelope in C5 format should be in a similar design, but does not have to be We need a strong business card for our company Brava-Lux.ch, logo is available. A black or dark background is desired, on which the logo Stark comes across. The letterhead and the envelope in C5 format should have a similar design.

Target Market(s)

Private customers as well as entrepreneurs

Contact Information for Business Card

E-mail: info@brava-lux.ch
Web.www.Brava-Lux.ch
Tel: +41 ( 0 ) 79 384 6027
Adresse:
Kellerweg 14
9405 Ostheim

Hier kann man Icons verwenden für Email,Tel und Adressse

Font styles to use
Other font styles liked:
• Dubai,bold

Colors

Designer to choose colors to be used in the design.

Requirements
Must have
• WOW effect
Nice to have
• R% 26 # 252; back business card with our service listings. - VEHICLE LABELING - SHOP WINDOW LABELING - STICKERS AND MUCH MORE ... in red color

```html
<!DOCTYPE html>
<html lang="de">
<head>
<meta charset="utf-8">
<title>Brava-Lux.ch – Visitenkarte</title>
<link rel="stylesheet" href="https://fonts.googleapis.com/css2?family=Lato:wght@400;700;900&display=swap">
<style>
  :root {
    --backdrop: #dedede;
    --card-white: #ffffff;
    --card-black: #070707;
    --accent: #fdc91f;
    --text-grey: #8a8a8a;
    --text-dark: #111111;
    --text-light: #ffffff;
  }
  * { margin: 0; padding: 0; box-sizing: border-box; }
  html, body {
    width: 1200px;
    height: 960px;
    overflow: hidden;
    background: var(--backdrop);
    font-family: "Lato", Arial, sans-serif;
  }
  .canvas { position: relative; width: 1200px; height: 960px; }

  .card {
    position: absolute;
    left: 281px;
    width: 655px;
    height: 374px;
    border-radius: 28px;
    overflow: hidden;
  }
  .card--front { top: 80px; background: var(--card-white); }
  .card--back { top: 506px; background: var(--card-black); }

  .front-pattern {
    position: absolute;
    top: 0;
    right: 0;
    width: 215px;
    height: 100%;
    background: linear-gradient(90deg, rgba(253, 201, 31, 0) 0%, rgba(253, 201, 31, 0.75) 35%, var(--accent) 100%);
  }

  .contact-block { position: absolute; left: 117px; top: 76px; }
  .person-name {
    font-size: 27px;
    font-weight: 700;
    color: var(--accent);
    line-height: 1.2;
  }
  .person-role {
    font-size: 18px;
    color: var(--text-grey);
    margin-top: 4px;
  }
  .company-name {
    font-size: 22px;
    font-weight: 900;
    color: var(--text-dark);
    margin-top: 18px;
    letter-spacing: 0.5px;
  }
  .address {
    font-size: 18px;
    color: var(--text-grey);
    line-height: 24px;
    margin-top: 4px;
    font-style: normal;
  }
  .contact-list { list-style: none; margin-top: 14px; }
  .contact-item {
    display: flex;
    align-items: center;
    gap: 8px;
    font-size: 18px;
    color: var(--text-grey);
    line-height: 24px;
  }
  .contact-icon { width: 14px; height: 14px; flex: none; }

  .brand-lockup {
    position: absolute;
    left: 50%;
    top: 50%;
    transform: translate(-50%, -50%);
    display: flex;
    align-items: center;
    gap: 22px;
  }
  .brand-mark { width: 44px; height: 44px; background: var(--accent); }
  .brand-name {
    font-size: 34px;
    font-weight: 900;
    color: var(--text-light);
    letter-spacing: 0.5px;
  }
</style>
</head>
<body>
<main class="canvas">
  <section class="card card--front">
    <div class="front-pattern" role="img" aria-label="Gelbes Wabenmuster aus Sechsecken am rechten Kartenrand"></div>
    <div class="contact-block">
      <p class="person-name">Lukas Meier</p>
      <p class="person-role">Managing Director</p>
      <p class="company-name">Brava-Lux.ch</p>
      <address class="address">Kellerweg 14<br>9405 Ostheim</address>
      <ul class="contact-list">
        <li class="contact-item">
          <svg class="contact-icon" viewBox="0 0 14 14"><path d="M2 12 C2 6 6 2 12 2 L12 4.5 C7.5 4.5 4.5 7.5 4.5 12 Z" fill="var(--accent)"/></svg>
          +41 ( 0 ) 79 384 6027
        </li>
        <li class="contact-item">
          <svg class="contact-icon" viewBox="0 0 14 14"><rect x="1" y="3.5" width="12" height="8" fill="var(--accent)"/><path d="M1 3.5 L7 8 L13 3.5" stroke="#fff" stroke-width="1.2" fill="none"/></svg>
          info@brava-lux.ch
        </li>
        <li class="contact-item">
          <svg class="contact-icon" viewBox="0 0 14 14"><g stroke="var(--accent)" stroke-width="1.2" fill="none"><circle cx="7" cy="7" r="5.6"/><ellipse cx="7" cy="7" rx="2.4" ry="5.6"/><path d="M1.4 7 H12.6 M2.4 4 H11.6 M2.4 10 H11.6"/></g></svg>
          www.Brava-Lux.ch
        </li>
      </ul>
    </div>
  </section>

  <section class="card card--back">
    <div class="brand-lockup">
      <span class="brand-mark"></span>
      <span class="brand-name">Brava-Lux.ch</span>
    </div>
  </section>
</main>
</body>
</html>
```